Criação de Papelaria Profissional para Beleza
" CLÍNICA DE ESTÉTICA COMPLETA, COM ÊNFASE EM ATENDIMENTO PRÊMIUM (salas exclusivas, máquinas próprias, ambiente aconchegante com forte conexão nordestina) Serviços ofertados: Estética corporal, facial, injetáveis e laser) SITE: https://brunelva.com.br/ "

```html
<!DOCTYPE html>
<html lang="pt-BR">
<head>
<meta charset="utf-8">
<title>Brunelva — Cartão de visita e cartão fidelidade</title>
<link rel="stylesheet" href="https://fonts.googleapis.com/css2?family=Cormorant+Garamond:wght@400;500&family=Montserrat:wght@300;400&display=swap">
<style>
  :root {
    --backdrop: #d07d75;
    --rose: #c8766e;
    --rose-soft: #d38a82;
    --blush: #f7e8e5;
    --ink-rose: #c2736b;
    --ink-muted: #b88a85;
    --white: #ffffff;
  }
  * { margin: 0; padding: 0; box-sizing: border-box; }
  html, body { width: 1200px; height: 1200px; overflow: hidden; }
  body {
    background: var(--backdrop);
    display: flex;
    align-items: center;
    justify-content: center;
    gap: 40px;
    font-family: "Montserrat", sans-serif;
  }
  .card {
    width: 520px;
    height: 300px;
    border-radius: 4px;
    position: relative;
    overflow: hidden;
  }

  /* Front */
  .card-front { background: var(--rose); }
  .front-decoration {
    position: absolute;
    left: -70px;
    bottom: -90px;
    width: 300px;
    height: 300px;
    border-radius: 50%;
    background: var(--rose-soft);
    opacity: 0.55;
  }
  .brand {
    position: absolute;
    top: 70px;
    left: 0;
    right: 0;
    display: flex;
    flex-direction: column;
    align-items: center;
    color: var(--white);
  }
  .brand-dot {
    width: 30px;
    height: 30px;
    border-radius: 50%;
    background: var(--white);
    margin-bottom: 16px;
  }
  .brand-name {
    font-family: "Cormorant Garamond", serif;
    font-weight: 500;
    font-size: 34px;
    letter-spacing: 0.42em;
    margin-right: -0.42em;
  }
  .brand-tagline {
    margin-top: 8px;
    font-size: 10px;
    letter-spacing: 0.2em;
    font-weight: 300;
  }

  /* Back */
  .card-back {
    background: var(--blush);
    padding: 30px 34px 0;
    color: var(--ink-rose);
    text-align: center;
  }
  .loyalty-title {
    font-family: "Cormorant Garamond", serif;
    font-weight: 500;
    font-size: 24px;
    letter-spacing: 0.16em;
  }
  .loyalty-note {
    margin-top: 6px;
    font-size: 10px;
    color: var(--ink-muted);
  }
  .stamp-grid {
    margin: 22px auto 0;
    display: grid;
    grid-template-columns: repeat(5, 36px);
    gap: 14px 26px;
    justify-content: center;
  }
  .stamp-slot {
    width: 36px;
    height: 42px;
    border: 1px solid var(--ink-muted);
    border-radius: 18px;
  }
  .loyalty-footer {
    margin-top: 18px;
    font-size: 10px;
    color: var(--ink-muted);
  }
  .contact-row {
    margin-top: 8px;
    display: flex;
    justify-content: center;
    gap: 40px;
    font-size: 10px;
    color: var(--ink-muted);
  }
  .contact-item { display: flex; align-items: center; gap: 6px; }
  .contact-item svg { width: 12px; height: 12px; }
  .social-mark {
    width: 11px;
    height: 11px;
    border: 1px solid var(--ink-muted);
    border-radius: 50%;
  }
  .back-band {
    position: absolute;
    left: 0;
    right: 0;
    bottom: 0;
    height: 8px;
    background: var(--rose);
  }
</style>
</head>
<body>
  <section class="card card-front" aria-label="Frente do cartão">
    <div class="front-decoration" role="img" aria-label="Marca decorativa em tom rosado suave"></div>
    <div class="brand">
      <div class="brand-dot"></div>
      <div class="brand-name">BRUNELVA</div>
      <div class="brand-tagline">brunelva estética</div>
    </div>
  </section>

  <section class="card card-back" aria-label="Verso do cartão fidelidade">
    <h1 class="loyalty-title">CARTÃO FIDELIDADE</h1>
    <p class="loyalty-note">Complete a cartela e ganhe 20% de desconto no próximo procedimento</p>
    <div class="stamp-grid">
      <div class="stamp-slot"></div><div class="stamp-slot"></div><div class="stamp-slot"></div><div class="stamp-slot"></div><div class="stamp-slot"></div>
      <div class="stamp-slot"></div><div class="stamp-slot"></div><div class="stamp-slot"></div><div class="stamp-slot"></div><div class="stamp-slot"></div>
    </div>
    <p class="loyalty-footer">Atendimento com horário marcado!</p>
    <div class="contact-row">
      <span class="contact-item">
        <svg viewBox="0 0 24 24" fill="none" stroke="#b88a85" stroke-width="2" stroke-linecap="round" stroke-linejoin="round" aria-hidden="true"><path d="M22 16.9v3a2 2 0 0 1-2.2 2 19.8 19.8 0 0 1-8.6-3.1 19.5 19.5 0 0 1-6-6A19.8 19.8 0 0 1 2.1 4.2 2 2 0 0 1 4.1 2h3a2 2 0 0 1 2 1.7c.1.9.4 1.8.7 2.7a2 2 0 0 1-.5 2.1L8 9.8a16 16 0 0 0 6 6l1.3-1.3a2 2 0 0 1 2.1-.4c.9.3 1.8.6 2.7.7a2 2 0 0 1 1.7 2z"/></svg>
        (00) 90412-5530
      </span>
      <span class="contact-item">
        <span class="social-mark"></span>
        @brunelvaestetica
      </span>
    </div>
    <div class="back-band"></div>
  </section>
</body>
</html>
```